Education Certificate

We need a modern yet professional Certificate for those who successfully pass / complete our online Training course.

There are various courses but ONE certificate design required.

the certificate needs to look extremely professional and of value.

```html
<!DOCTYPE html>
<html lang="en">
<head>
<meta charset="utf-8">
<title>Certificate of Achievement</title>
<link href="https://fonts.googleapis.com/css2?family=Playfair+Display:wght@700&family=Cinzel:wght@400;600&family=Poppins:wght@400;500&family=Great+Vibes&display=swap" rel="stylesheet">
<style>
  :root {
    --paper: #ececeb;
    --gold: #c9a54c;
    --gold-light: #dcc071;
    --gold-deep: #a57f35;
    --ink: #2e2e2e;
    --ink-soft: #3a3a3a;
  }
  html, body {
    margin: 0;
    padding: 0;
    width: 1200px;
    height: 799px;
    overflow: hidden;
    background: var(--paper);
  }
  .certificate {
    position: relative;
    width: 1200px;
    height: 799px;
    background: var(--paper);
    color: var(--ink);
  }
  .frame {
    position: absolute;
    inset: 0;
  }
  .corner-ornament {
    position: absolute;
    width: 122px;
    height: 116px;
    background: linear-gradient(135deg, var(--gold-light), var(--gold-deep));
    opacity: 0.55;
  }
  .corner-ornament.top-left { left: 34px; top: 27px; border-radius: 4px 0 60px 0; }
  .corner-ornament.top-right { right: 34px; top: 27px; border-radius: 0 4px 0 60px; }
  .corner-ornament.bottom-left { left: 34px; bottom: 27px; border-radius: 0 60px 0 4px; }
  .corner-ornament.bottom-right { right: 34px; bottom: 27px; border-radius: 60px 0 4px 0; }

  .title {
    position: absolute;
    top: 98px;
    left: 0;
    width: 100%;
    margin: 0;
    text-align: center;
    font-family: "Playfair Display", serif;
    font-weight: 700;
    font-size: 68px;
    letter-spacing: 3px;
    line-height: 1;
    color: var(--ink);
  }
  .subtitle {
    position: absolute;
    top: 176px;
    left: 0;
    width: 100%;
    text-align: center;
    font-family: "Cinzel", serif;
    font-weight: 400;
    font-size: 20px;
    letter-spacing: 4.5px;
    color: var(--ink-soft);
  }
  .presented {
    position: absolute;
    top: 255px;
    left: 0;
    width: 100%;
    text-align: center;
    font-family: "Poppins", sans-serif;
    font-weight: 500;
    font-size: 13px;
    letter-spacing: 0.9px;
    color: var(--ink);
  }
  .recipient {
    position: absolute;
    top: 282px;
    left: 0;
    width: 100%;
    text-align: center;
    font-family: "Great Vibes", cursive;
    font-size: 96px;
    line-height: 1.1;
    background: linear-gradient(180deg, var(--gold-light), var(--gold-deep));
    -webkit-background-clip: text;
    background-clip: text;
    color: transparent;
  }
  .description {
    position: absolute;
    top: 422px;
    left: 280px;
    width: 640px;
    margin: 0;
    text-align: center;
    font-family: "Poppins", sans-serif;
    font-size: 13.5px;
    line-height: 26px;
    color: var(--ink);
  }
  .award-seal {
    position: absolute;
    left: 517px;
    top: 546px;
    width: 166px;
    height: 166px;
    border-radius: 50%;
    background: radial-gradient(circle, var(--gold-light) 0%, var(--gold) 60%, var(--gold-deep) 100%);
    opacity: 0.6;
  }
  .sign-label {
    position: absolute;
    top: 664px;
    width: 220px;
    text-align: center;
    font-family: "Cinzel", serif;
    font-weight: 600;
    font-size: 17px;
    letter-spacing: 3px;
    color: var(--ink-soft);
  }
  .sign-label.date { left: 193px; }
  .sign-label.signature { left: 786px; }
</style>
</head>
<body>
<main class="certificate">
  <svg class="frame" width="1200" height="799" viewBox="0 0 1200 799" aria-hidden="true">
    <defs>
      <linearGradient id="goldLine" x1="0" x2="1">
        <stop offset="0" stop-color="#a57f35"/>
        <stop offset="0.5" stop-color="#d6b867"/>
        <stop offset="1" stop-color="#a57f35"/>
      </linearGradient>
    </defs>
    <g fill="#c9a54c" stroke="#c9a54c">
      <!-- top and bottom borders -->
      <g class="border-top">
        <line x1="165" y1="48" x2="305" y2="48" stroke-width="2"/>
        <line x1="895" y1="48" x2="1035" y2="48" stroke-width="2"/>
        <line x1="325" y1="48" x2="875" y2="48" stroke-width="2.2" stroke-dasharray="0.1 8" stroke-linecap="round"/>
        <path d="M236 40 L246 48 L236 56 L226 48 Z" stroke="none"/>
        <circle cx="236" cy="48" r="3" stroke="none"/>
        <path d="M964 40 L974 48 L964 56 L954 48 Z" stroke="none"/>
      </g>
      <g class="border-bottom">
        <line x1="165" y1="748" x2="305" y2="748" stroke-width="2"/>
        <line x1="895" y1="748" x2="1035" y2="748" stroke-width="2"/>
        <line x1="325" y1="748" x2="875" y2="748" stroke-width="2.2" stroke-dasharray="0.1 8" stroke-linecap="round"/>
        <path d="M236 740 L246 748 L236 756 L226 748 Z" stroke="none"/>
        <path d="M964 740 L974 748 L964 756 L954 748 Z" stroke="none"/>
      </g>
      <!-- side borders -->
      <line x1="52" y1="155" x2="52" y2="645" stroke-width="2"/>
      <line x1="1148" y1="155" x2="1148" y2="645" stroke-width="2"/>
      <path d="M52 210 L60 222 L52 234 L44 222 Z M52 575 L60 587 L52 599 L44 587 Z" stroke="none"/>
      <path d="M1148 210 L1156 222 L1148 234 L1140 222 Z M1148 575 L1156 587 L1148 599 L1140 587 Z" stroke="none"/>
      <!-- subtitle rules -->
      <line x1="342" y1="188" x2="426" y2="188" stroke-width="2"/>
      <path d="M338 188 L346 183 L354 188 L346 193 Z" stroke="none"/>
      <line x1="774" y1="188" x2="858" y2="188" stroke-width="2"/>
      <path d="M862 188 L854 183 L846 188 L854 193 Z" stroke="none"/>
      <!-- diamond row -->
      <g stroke="none">
        <path d="M552 223 L557 228 L552 233 L547 228 Z"/>
        <path d="M584 223 L589 228 L584 233 L579 228 Z"/>
        <path d="M615 223 L620 228 L615 233 L610 228 Z"/>
        <path d="M647 223 L652 228 L647 233 L642 228 Z"/>
      </g>
      <!-- name underline -->
      <line x1="262" y1="398" x2="938" y2="398" stroke="url(#goldLine)" stroke-width="2"/>
      <path d="M257 398 L266 393 L275 398 L266 403 Z" stroke="none"/>
      <path d="M943 398 L934 393 L925 398 L934 403 Z" stroke="none"/>
      <!-- signature lines -->
      <path d="M203 651 Q303 648 404 651 Q303 654 203 651 Z" stroke="none"/>
      <path d="M795 651 Q896 648 997 651 Q896 654 795 651 Z" stroke="none"/>
    </g>
  </svg>

  <div class="corner-ornament top-left" role="img" aria-label="Gold filigree corner ornament"></div>
  <div class="corner-ornament top-right" role="img" aria-label="Gold filigree corner ornament"></div>
  <div class="corner-ornament bottom-left" role="img" aria-label="Gold filigree corner ornament"></div>
  <div class="corner-ornament bottom-right" role="img" aria-label="Gold filigree corner ornament"></div>

  <h1 class="title">CERTIFICATE</h1>
  <div class="subtitle">OF ACHIEVEMENT</div>
  <div class="presented">THIS CERTIFICATE IS PROUDLY PRESENTED TO</div>
  <div class="recipient">Name Surname</div>
  <p class="description">Lorem ipsum dolor sit amet, consectetuer adipiscing elit, sed diam nonummy nibh euismod tincidunt ut laoreet dolore magna aliquam erat volutpat. Ut wisi enim ad minim veniam.</p>

  <div class="award-seal" role="img" aria-label="Gold laurel award seal"></div>

  <div class="sign-label date">DATE</div>
  <div class="sign-label signature">SIGNATURE</div>
</main>
</body>
</html>
```